Business card for a vending machine business

I need a business card for my vending machine business. The name is Kestrel Snackworks, LLC. The card is one-sided, and landscape format. Not portrait.

The information for the card is as follows:

Dana Whitlow
Owner
(555) 314-2907
Kestrelsnackworks.example
Info@kestrelsnackworks.example

I'd like colors and design elements to match what's in my logo and company name. I'd like to have the checkered flag or racing stripe if possible You can use a border if youd like. You can use a background color if it looks nice and doesn't clash with the logo
Use your creativity. But a white background is perfectly fine. The card can be as simple, yet gets the point across to match the company name and logo.

I uploaded a copy of my logo. I also uploaded a businesses card I started to create, but since it was missing something, I gave up. Another upload has a red thunderbolt and the checkerer flag. Those two uploads are for inspiration. Again, please make sure to make the card landscape, not portrait. Thank you, designers. Good luck to all.

```html
<!DOCTYPE html>
<html lang="en">
<head>
<meta charset="utf-8">
<title>Kestrel Snackworks – Business Card</title>
<link href="https://fonts.googleapis.com/css2?family=Saira:wght@400;600;700&display=swap" rel="stylesheet">
<style>
  :root {
    --stage: #9a9a9a;
    --card: #ffffff;
    --race-red: #ee0000;
    --ink: #111111;
    --flag-dark: #1a1a1a;
    --flag-light: #6a6a6a;
    --white: #ffffff;
  }
  * { margin: 0; padding: 0; box-sizing: border-box; }
  html, body { width: 1200px; height: 1017px; overflow: hidden; }
  body { background: var(--stage); font-family: "Saira", sans-serif; position: relative; }

  .card { position: absolute; left: 321px; width: 556px; height: 318px; background: var(--card); overflow: hidden; }
  .card--front { top: 135px; }
  .card--back { top: 547px; }
  .card__art { position: absolute; inset: 0; width: 100%; height: 100%; }

  .wordmark { position: absolute; display: flex; flex-direction: column; align-items: center; justify-content: center; text-align: center; color: var(--race-red); font-weight: 700; text-transform: uppercase; line-height: 1; }
  .card--front .wordmark { left: 128px; top: 49px; width: 306px; height: 213px; font-size: 38px; }
  .card--back .wordmark { left: 30px; top: 52px; width: 190px; height: 132px; font-size: 24px; }

  .contact-name { position: absolute; left: 329px; top: 58px; color: var(--white); font-weight: 700; font-size: 24px; line-height: 1; letter-spacing: 0.3px; }
  .contact-role { position: absolute; left: 329px; top: 84px; color: var(--white); font-weight: 400; font-size: 14px; line-height: 1; }

  .contact-line { position: absolute; color: var(--ink); font-weight: 600; font-size: 12.5px; line-height: 1; transform: translateY(-50%); white-space: nowrap; }
  .contact-line--phone { left: 298px; top: 131px; }
  .contact-line--web { left: 325px; top: 165px; }
  .contact-line--mail { left: 352px; top: 198px; font-size: 12px; }
</style>
</head>
<body>

<section class="card card--front" aria-label="Card front">
  <svg class="card__art" viewBox="0 0 556 318" aria-hidden="false">
    <defs>
      <linearGradient id="flagToneFront" x1="0" y1="0" x2="1" y2="1">
        <stop offset="0" stop-color="var(--flag-dark)"/>
        <stop offset="1" stop-color="var(--flag-light)"/>
      </linearGradient>
    </defs>
    <polygon role="img" aria-label="Chequered racing flag pattern" fill="url(#flagToneFront)"
      points="0,0 68,0 62,58 123,58 112,115 70,115 56,210 122,210 110,292 76,292 70,318 0,318"/>
    <polygon role="img" aria-label="Chequered racing flag pattern" fill="url(#flagToneFront)"
      points="503,0 556,0 556,318 542,318 533,292 443,292 456,210 478,210 494,125 445,125 460,58 493,58"/>
  </svg>
  <div class="wordmark">Kestrel<br>Snackworks</div>
</section>

<section class="card card--back" aria-label="Card back">
  <svg class="card__art" viewBox="0 0 556 318">
    <defs>
      <linearGradient id="flagToneBack" x1="0" y1="0" x2="1" y2="1">
        <stop offset="0" stop-color="var(--flag-dark)"/>
        <stop offset="1" stop-color="var(--flag-light)"/>
      </linearGradient>
    </defs>
    <polygon class="name-band" fill="var(--race-red)" points="310,55 556,55 556,107 298,107"/>
    <polygon class="icon-tile" fill="var(--race-red)" points="259,114 291,114 285,147 253,147"/>
    <polygon class="icon-tile" fill="var(--race-red)" points="286,148 318,148 312,181 280,181"/>
    <polygon class="icon-tile" fill="var(--race-red)" points="312,182 345,182 339,214 306,214"/>
    <!-- phone -->
    <path fill="var(--white)" d="M265,122 c2,-1 4,0 5,2 l2,4 c0,2 -1,3 -2,4 c1,3 4,6 7,7 c1,-1 2,-2 4,-2 l4,2 c2,1 2,3 1,5 l-2,2 c-8,1 -19,-10 -20,-20 z"/>
    <!-- globe -->
    <g fill="none" stroke="var(--white)" stroke-width="1.6">
      <circle cx="299" cy="164.5" r="10"/>
      <ellipse cx="299" cy="164.5" rx="4.5" ry="10"/>
      <line x1="289" y1="164.5" x2="309" y2="164.5"/>
    </g>
    <!-- envelope -->
    <g fill="none" stroke="var(--white)" stroke-width="1.6">
      <rect x="315" y="191" width="21" height="14"/>
      <polyline points="315,191 325.5,199 336,191"/>
      <line x1="315" y1="205" x2="322" y2="197"/>
      <line x1="336" y1="205" x2="329" y2="197"/>
    </g>
    <polygon role="img" aria-label="Chequered racing flag pattern" fill="url(#flagToneBack)"
      points="0,214 238,214 245,182 282,182 275,214 371,214 364,248 398,248 388,282 364,282 357,314 0,314"/>
  </svg>

  <div class="wordmark">Kestrel<br>Snackworks</div>

  <p class="contact-name">DANA WHITLOW</p>
  <p class="contact-role">Owner</p>
  <p class="contact-line contact-line--phone">(555) 314-2907</p>
  <p class="contact-line contact-line--web">Kestrelsnackworks.example</p>
  <p class="contact-line contact-line--mail">Info@kestrelsnackworks.example</p>
</section>

</body>
</html>
```